Tallow Ridge Snacks is looking for a wrapper design for our flagship protein bar. A sleek and simple, yet powerful design is a must. A company that has a no BS attitude, no flashy artwork and straight to the point advertising is key. Focusing on Bodybuilders and Powerlifters, the wrapper does not need to appeal to the mass market. A dark, simple, and powerful vibe must be achieved. Less is more

Target Market(s)

Body Builders and Powerlifters

Industry/Entity Type

Supplement

Font styles to use
Decorative

Colors

Designer to choose colors to be used in the design.

Requirements
Must have
• Refer to "Legal Label Requirements" document.
• Refer to "Template Drawn" or "Wrapper.ai" for dimensions.
• *Must have the "Tallow Bar" logo stamped somewhere on the front of the bar**
• Sleek and powerful design
• Neutral /dark colors and possible accents with logo colors (use sparingly)
• Flavor of bar "Peanut Butter Crisp" must be displayed somewhere. Simple graphic can be included if goes well with overall design.
• Wrapper will be foil, so please make use of metallic effects by leaving sections/outlines transparent.
• Claims: (State it uses "Hydrolyzed Whey Protein" and contains 25g's of protein and only 6g's of sugar, as well as only real ingredients (These must be in French as well)
• Proudly Canadian stamp with flag somewhere.
• Social Media Icons (Instagram,Facebook) as well as website "tallowbarsnx.ca)
• Design must be able to work with future bar flavors, with only altering colors/flavor graphic (if necessary)
• *Will Include Nutritional Label and Ingredient List at a later date*
Nice to have
• I think a cool graphic of a simple hand and hammer outline using the metallic effect would be cool. Something that resembles the act of "forging metal" while demonstrating power, but isn't too distracting.
• A label mock up to see a general bar idea
Should not have
• Flashy/godly designs

```html
<!DOCTYPE html>
<html lang="en">
<head>
<meta charset="utf-8">
<title>Tallow Bar – Peanut Butter Crisp Wrapper</title>
<link href="https://fonts.googleapis.com/css2?family=Bebas+Neue&family=Fira+Sans+Condensed:wght@500;600;700&display=swap" rel="stylesheet">
<style>
  :root {
    --backdrop: #d3d1d1;
    --wrapper-dark: #3b2a22;
    --wrapper-deep: #2e201a;
    --flavor-band: #86654a;
    --flavor-band-light: #9a7857;
    --silver: #d9d9d9;
    --accent-red: #e1262b;
    --headline-tan: #a88c70;
    --text-light: #f4efe9;
    --text-shadowed: #4a3526;
  }
  * { margin: 0; padding: 0; box-sizing: border-box; }
  html, body { width: 1200px; height: 1000px; overflow: hidden; background: var(--backdrop); }
  .canvas { position: relative; width: 1200px; height: 1000px; }
  .wrapper-shape { position: absolute; left: 0; top: 0; }
  .front { position: absolute; inset: 0; font-family: "Fira Sans Condensed", sans-serif; }

  .brand-name {
    position: absolute; left: 433px; top: 363px; width: 98px; height: 30px;
    display: flex; align-items: center; justify-content: center; gap: 6px;
    font-family: "Fira Sans Condensed", sans-serif; font-weight: 600;
    font-size: 14px; letter-spacing: 2px; color: var(--text-light); text-transform: uppercase;
  }
  .brand-square { width: 7px; height: 7px; background: var(--accent-red); }

  .rule { position: absolute; left: 420px; width: 156px; height: 2px; background: var(--accent-red); }
  .rule-top { top: 410px; }
  .rule-bottom { top: 521px; }

  .headline { position: absolute; left: 420px; font-family: "Bebas Neue", sans-serif; line-height: 1; }
  .headline-protein { top: 418px; font-size: 56px; color: var(--headline-tan); }
  .headline-bars { top: 467px; font-size: 56px; color: var(--accent-red); }
  .headline-french {
    position: absolute; left: 421px; top: 528px; font-family: "Bebas Neue", sans-serif;
    font-size: 21px; color: var(--text-light); letter-spacing: 0.3px;
  }

  .forging-graphic {
    position: absolute; left: 675px; top: 356px; width: 118px; height: 150px;
    border-radius: 18px;
    background: radial-gradient(circle at 50% 45%, #8c7053 0%, #5a4332 60%, rgba(59,42,34,0) 100%);
  }
  .claim-whey {
    position: absolute; left: 676px; top: 530px; font-family: "Bebas Neue", sans-serif;
    font-size: 18px; color: var(--text-light); letter-spacing: 0.3px;
  }

  .flavor-name {
    position: absolute; left: 410px; top: 572px; font-weight: 700; font-size: 19px; color: var(--text-light);
  }
  .flavor-french {
    position: absolute; left: 410px; top: 594px; font-weight: 700; font-size: 13px;
    color: var(--text-shadowed); height: 12px; overflow: hidden; line-height: 15px;
  }
  .stats { position: absolute; left: 737px; top: 572px; display: flex; color: var(--text-light); }
  .stat { display: flex; flex-direction: column; line-height: 1; }
  .stat-value { font-weight: 700; font-size: 20px; }
  .stat-label { font-weight: 500; font-size: 9px; margin-top: 3px; }
  .stat-divider { width: 1px; height: 34px; background: var(--text-light); margin: 0 7px; }
</style>
</head>
<body>
<div class="canvas">
  <svg class="wrapper-shape" width="1200" height="1000" viewBox="0 0 1200 1000" aria-hidden="true">
    <defs>
      <linearGradient id="flavorBand" x1="0" y1="0" x2="0" y2="1">
        <stop offset="0" stop-color="var(--flavor-band-light)"/>
        <stop offset="1" stop-color="var(--flavor-band)"/>
      </linearGradient>
      <clipPath id="wrapperOutline">
        <path d="M165 318 L235 318 L235 338 L965 338 L965 318 L1035 318
                 L1035 645 L965 645 L965 622 L235 622 L235 645 L165 645 Z"/>
      </clipPath>
    </defs>
    <g clip-path="url(#wrapperOutline)">
      <rect x="160" y="310" width="880" height="250" fill="var(--wrapper-dark)"/>
      <rect x="160" y="560" width="880" height="90" fill="url(#flavorBand)"/>
      <rect x="160" y="561" width="880" height="6" fill="var(--silver)"/>
      <rect x="160" y="310" width="75" height="340" fill="var(--wrapper-deep)" opacity="0.35"/>
      <rect x="965" y="310" width="75" height="340" fill="var(--wrapper-deep)" opacity="0.35"/>
    </g>
    <path d="M165 318 l4 6 l-4 6 l4 6 l-4 6 l4 6 l-4 6 l4 6 l-4 6 l4 6 l-4 6 l4 6 l-4 6" fill="none" stroke="var(--backdrop)" stroke-width="2"/>
    <path d="M1035 318 l-4 6 l4 6 l-4 6 l4 6 l-4 6 l4 6 l-4 6 l4 6 l-4 6 l4 6 l-4 6 l4 6" fill="none" stroke="var(--backdrop)" stroke-width="2"/>
  </svg>

  <div class="front">
    <div class="brand-name"><span class="brand-square"></span>Tallow Bar</div>

    <div class="rule rule-top"></div>
    <div class="headline headline-protein">Protein</div>
    <div class="headline headline-bars">Bars</div>
    <div class="rule rule-bottom"></div>
    <div class="headline-french">Barre de protéines</div>

    <div class="forging-graphic" role="img" aria-label="Metallic outline of a fist gripping a forging hammer"></div>
    <div class="claim-whey">Hydrolyzed Whey Protein</div>

    <div class="flavor-name">Peanut Butter Crisp</div>
    <div class="flavor-french">Crisp au beurre d'arachide</div>

    <div class="stats">
      <div class="stat"><span class="stat-value">25g</span><span class="stat-label">of protein</span></div>
      <div class="stat-divider"></div>
      <div class="stat"><span class="stat-value">6g</span><span class="stat-label">of sugar</span></div>
    </div>
  </div>
</div>
</body>
</html>
```